Brightstone Roofing Business Card

This is my current business card. But I’d like to make some changes. Somewhere on the card I’d like to list some of the services we offer. Maybe on the back? But I’d still like to keep the red. White and black modern look.

-residential & commercial roofing
-Roof Repairs & Maintenance
-Storm Damage & Insurance Claims specialist
-Christmas Lights and permanent Christmas lights
Fencing. Windows. Gutters. Siding. Sheetrock, painting.

```html
<!DOCTYPE html>
<html lang="en">
<head>
<meta charset="utf-8">
<title>Brightstone Roofing Business Card</title>
<link href="https://fonts.googleapis.com/css2?family=Michroma&family=Montserrat:wght@400;500&display=swap" rel="stylesheet">
<style>
  :root {
    --red: #e0141e;
    --black: #1b1b1b;
    --ink: #111111;
    --white: #ffffff;
    --stage: #e9e7e4;
    --heading: "Michroma", sans-serif;
    --body: "Montserrat", sans-serif;
  }
  * { margin: 0; padding: 0; box-sizing: border-box; }
  html, body { width: 900px; height: 1200px; overflow: hidden; }
  body { background: var(--stage); position: relative; font-family: var(--body); }

  .card {
    position: absolute;
    border-radius: 22px;
    overflow: hidden;
    box-shadow: 0 6px 18px rgba(0,0,0,.25);
  }
  .card--front { left: 80px; top: 131px; width: 742px; height: 441px; background: var(--white); }
  .card--back { left: 78px; top: 638px; width: 744px; height: 440px; background: var(--black); }

  .brand-mark {
    position: absolute;
    border-radius: 50%;
    background: var(--red);
  }
  .card--front .brand-mark { left: 528px; top: 35px; width: 124px; height: 124px; }
  .card--back .brand-mark { left: 277px; top: 57px; width: 190px; height: 190px; }

  .brand-name {
    position: absolute;
    font-family: var(--heading);
    color: var(--red);
    text-align: center;
    line-height: 1.3;
  }
  .card--front .brand-name { left: 440px; top: 175px; width: 300px; font-size: 22px; }
  .card--back .brand-name { left: 0; top: 270px; width: 744px; font-size: 38px; }

  .person { position: absolute; left: 34px; top: 204px; }
  .person__name { font-family: var(--heading); font-size: 22px; color: var(--ink); letter-spacing: .5px; }
  .person__name span { color: var(--red); }
  .person__role { font-size: 15px; color: var(--ink); margin-top: 4px; }

  .divider { position: absolute; left: 30px; top: 259px; width: 686px; height: 1.5px; background: var(--red); }

  .services {
    position: absolute; right: 30px; top: 277px;
    list-style: none; text-align: right;
    font-size: 15.5px; color: var(--ink); line-height: 1.3;
  }
  .services li { position: relative; padding-right: 8px; margin-bottom: 6px; }
  .services li::after {
    content: ""; position: absolute; right: -8px; top: 50%;
    width: 6px; height: 6px; border-radius: 50%; background: var(--red);
  }

  .contact { position: absolute; left: 34px; top: 330px; list-style: none; font-size: 15.5px; color: var(--ink); }
  .contact li { display: flex; align-items: center; gap: 8px; height: 28px; }
  .contact svg { width: 16px; height: 16px; fill: var(--red); flex: none; }

  .footer-band { position: absolute; left: 0; bottom: 0; width: 742px; height: 22px; }
</style>
</head>
<body>

<section class="card card--front">
  <div class="brand-mark"></div>
  <div class="brand-name">BRIGHTSTONE<br>ROOFING CO.</div>

  <div class="person">
    <div class="person__name">DANIEL <span>REYES</span></div>
    <div class="person__role">Owner</div>
  </div>

  <div class="divider"></div>

  <ul class="services">
    <li>residential &amp; commercial roofing</li>
    <li>Roof Repairs &amp; Maintenance</li>
    <li>Storm Damage &amp;<br>Insurance Claims specialist</li>
    <li>Fencing. Windows. Gutters.<br>Siding. Sheetrock, painting</li>
  </ul>

  <ul class="contact">
    <li>
      <svg viewBox="0 0 24 24"><path d="M6.6 10.8a15 15 0 0 0 6.6 6.6l2.2-2.2c.3-.3.7-.4 1-.2 1.1.4 2.3.6 3.6.6.6 0 1 .4 1 1V20c0 .6-.4 1-1 1A17 17 0 0 1 3 4c0-.6.4-1 1-1h3.5c.6 0 1 .4 1 1 0 1.3.2 2.5.6 3.6.1.3 0 .7-.2 1z"/></svg>
      682-555-0193
    </li>
    <li>
      <svg viewBox="0 0 24 24"><path d="M2 5h20v2l-10 6L2 7z M2 9l10 6 10-6v10H2z"/></svg>
      dan@brightstoneroofing.com
    </li>
    <li>
      <svg viewBox="0 0 24 24"><circle cx="12" cy="12" r="10"/><path d="M2 12h20M12 2c3 3 3 17 0 20M12 2c-3 3-3 17 0 20" stroke="#fff" stroke-width="1.5" fill="none"/></svg>
      www.brightstoneroofing.com
    </li>
  </ul>

  <svg class="footer-band" viewBox="0 0 742 22" preserveAspectRatio="none">
    <polygon points="0,0 378,0 356,22 0,22" fill="var(--black)"/>
    <polygon points="392,0 742,0 742,22 370,22" fill="var(--red)"/>
  </svg>
</section>

<section class="card card--back">
  <div class="brand-mark"></div>
  <div class="brand-name">BRIGHTSTONE<br>ROOFING CO.</div>
</section>

</body>
</html>
```